Kitesurf Weather Forecast Application Needs an Advertising Banner

We need an Advertising Banner for our iOS Kitesurf Weather Forecast Application. The application name is GustMapper and you can download it from the Plum Depot.

https://apps.plumdepot-market.com/app/gustmapper-breeze-and-sky-outlook/id804417392?mt=8

The banner should have the logo of our application, which can be either found from the Plum Depot or uploaded on this post. It should describe what our app does with either words or graphic story. GustMapper is a weather forecast application for Kitesurfers. As the banner is small, animated gifs will also be considered.

We need the following sizes 320x50 and 728x90. The banner will be uploaded to tavlo. Tavlo accepts images in PNG, JPEG and GIF. We want it in one of the formats that can be uploaded to TavLo and vector .ai so we can make changed if necessary in the future.

On tap the banner will open Plum Depot on the user's device and present GustMapper.

06/09. I added a screenshot from an application that the banner will be added. The screenshot is from an Lumafon 4 Max (it is from a big device). The red area on the bottom is where the advert will go and it should be readable.

Target Market(s)

Banner will be displayed in other iOS Applications. One of them is Rigging Reckoner https://apps.plumdepot-market.com/us/app/rigging-reckoner/id937206148?mt=8

Industry/Entity Type

Advertising

Font styles to use
Other font styles liked:
• San Francisco

Requirements
Must have
• GustMapper logo and communicate a clear message on what the application does. GustMapper is a weather forecast application for Kitesurfers. If you want to find more information please visit the PlumDepot link provided.
Nice to have
• Animated gif will be nice to have, as the banner is small and it maybe difficult to communicate the message required.
Should not have
• We prefer something minimal and along the lines of our application design.

```html
<!DOCTYPE html>
<html lang="en">
<head>
<meta charset="utf-8">
<title>GustMapper Banner</title>
<link rel="stylesheet" href="https://fonts.googleapis.com/css2?family=Roboto:wght@500&display=swap">
<style>
  :root {
    --navy: #22308f;
    --sky-top: #8fbfe6;
    --sky-bottom: #e6f1fa;
    --sea: #6f9fc4;
    --white: #ffffff;
    --badge: #111111;
    --badge-edge: #8a8a8a;
    --card-fill: #eef5fb;
    --card-edge: #22308f;
    --card-text: #22308f;
  }
  html, body {
    margin: 0;
    padding: 0;
    overflow: hidden;
  }
  .banner {
    position: relative;
    width: 1200px;
    height: 148px;
    overflow: hidden;
    font-family: "Roboto", Arial, sans-serif;
    font-weight: 500;
    color: var(--white);
    background: var(--navy);
  }
  .scene-photo {
    position: absolute;
    left: 700px;
    top: 0;
    width: 500px;
    height: 148px;
    background: linear-gradient(180deg, var(--sky-top) 0%, var(--sky-bottom) 70%, var(--sea) 100%);
  }
  .navy-field {
    position: absolute;
    left: 0;
    top: 0;
  }
  .feature {
    position: absolute;
    transform: translateX(-50%);
    text-align: center;
    white-space: nowrap;
    font-size: 20px;
    line-height: 24px;
    text-shadow: 0 1px 2px rgba(0,0,0,0.6);
  }
  .feature .line {
    display: flex;
    align-items: center;
    justify-content: center;
    gap: 8px;
  }
  .feature svg { flex: none; }
  .feature-weekly { left: 150px; top: 20px; }
  .feature-live { left: 150px; top: 92px; }
  .feature-custom { left: 412px; top: 16px; }
  .feature-map { left: 412px; top: 90px; }
  .feature-detail { left: 651px; top: 12px; }
  .store-badge {
    position: absolute;
    top: 16px;
    width: 92px;
    height: 30px;
    border-radius: 5px;
    background: var(--badge);
    border: 1px solid var(--badge-edge);
  }
  .badge-plum { left: 882px; }
  .badge-seed { left: 984px; }
  .weather-icon {
    position: absolute;
    left: 1110px;
    top: 4px;
  }
  .app-card {
    position: absolute;
    left: 882px;
    top: 66px;
    width: 310px;
    height: 76px;
    box-sizing: border-box;
    background: var(--card-fill);
    border: 2px solid var(--card-edge);
    display: flex;
    align-items: center;
    justify-content: center;
    gap: 12px;
  }
  .app-dot {
    width: 22px;
    height: 22px;
    border-radius: 50%;
    background: var(--card-text);
    flex: none;
  }
  .app-name {
    color: var(--card-text);
    font-size: 26px;
    line-height: 30px;
  }
</style>
</head>
<body>
<div class="banner">
  <div class="scene-photo" role="img" aria-label="Kitesurfer flying a kite above the sea under a bright sky"></div>

  <svg class="navy-field" width="1200" height="148" viewBox="0 0 1200 148" aria-hidden="true">
    <defs>
      <linearGradient id="navyFade" x1="0" y1="0" x2="1" y2="0">
        <stop offset="0" stop-color="#1f2c88"/>
        <stop offset="1" stop-color="#2a3a9e"/>
      </linearGradient>
    </defs>
    <path d="M0 0 H870 C850 50 805 100 780 148 H0 Z" fill="url(#navyFade)"/>
  </svg>

  <div class="feature feature-weekly">
    <div class="line">
      <svg width="28" height="18" viewBox="0 0 28 18"><path d="M7 16 a6 6 0 0 1 1-11 a8 8 0 0 1 14 3 a4 4 0 0 1 0 8 Z" fill="none" stroke="#fff" stroke-width="2"/></svg>
      <span>Weekly Forecast</span>
    </div>
    <div class="line">Showing only Kiteable Spots</div>
  </div>

  <div class="feature feature-live">
    <div class="line">
      <svg width="12" height="24" viewBox="0 0 12 24"><rect x="4" y="1" width="4" height="15" rx="2" fill="none" stroke="#fff" stroke-width="1.6"/><circle cx="6" cy="19" r="4" fill="#fff"/></svg>
      <span>Live Weather</span>
    </div>
    <div class="line">Check Out Live Stations</div>
  </div>

  <div class="feature feature-custom">
    <div class="line">Customized Forecast for</div>
    <div class="line" style="margin-top:8px">
      <svg width="22" height="22" viewBox="0 0 22 22" stroke="#fff" stroke-width="2" stroke-linecap="round"><path d="M11 1 V21 M2 6 L20 16 M2 16 L20 6"/></svg>
      <span>KiteSurfers</span>
    </div>
  </div>

  <div class="feature feature-map">
    <div class="line">
      <svg width="22" height="22" viewBox="0 0 22 22" stroke="#fff" stroke-width="2" stroke-linecap="round"><circle cx="11" cy="11" r="4.5" fill="#fff"/><path d="M11 1 V3 M11 19 V21 M1 11 H3 M19 11 H21 M4 4 L5.5 5.5 M16.5 16.5 L18 18 M4 18 L5.5 16.5 M16.5 5.5 L18 4"/></svg>
      <span>Weather on Map</span>
    </div>
    <div class="line">Get Forecasr abd Live Data</div>
  </div>

  <div class="feature feature-detail">
    <div class="line">
      <svg width="40" height="44" viewBox="0 0 40 44"><path d="M9 26 a8 8 0 0 1 2-15 a11 11 0 0 1 20 4 a6 6 0 0 1 0 11 Z" fill="#fff"/><path d="M13 31 l-2 6 M20 31 l-2 6 M27 31 l-2 6" stroke="#fff" stroke-width="2.5" stroke-linecap="round"/></svg>
    </div>
    <div class="line">Detailed Weather</div>
    <div class="line">See Hourly Forecast &amp; Live</div>
  </div>

  <div class="store-badge badge-plum" role="img" aria-label="Download on Plum Depot"></div>
  <div class="store-badge badge-seed" role="img" aria-label="Get it on Seed Shelf"></div>

  <svg class="weather-icon" width="80" height="56" viewBox="0 0 80 56" aria-hidden="true">
    <path d="M18 36 a12 12 0 0 1 3-23 a17 17 0 0 1 31 5 a9 9 0 0 1 0 18 Z" fill="#ffffff" stroke="#9bb8d4" stroke-width="1.5"/>
    <path d="M26 42 l-3 8 M38 42 l-3 8 M50 42 l-3 8" stroke="#5a86b8" stroke-width="3" stroke-linecap="round"/>
  </svg>

  <div class="app-card">
    <span class="app-dot" aria-hidden="true"></span>
    <span class="app-name">GustMapper</span>
  </div>
</div>
</body>
</html>
```